2in1 Bartender & Sommelier needs a business card

I need a business card. I worked as a bartender in many places but I just finished a sommelier school and I would like a new business card. I like minimal design, natural materials and something what makes the people think :) I try to be creative in cocktail making, like little mixology, little twist on recipes... I like to travel and discover new places, cultures and of course interesting drinks and improve continously...live a little bit crazy life. And I like what I do...

Target Market(s)

restaurant/winebar managers, winemakers, other sommeliers and bartenders, people who work in food and beverage sector

Industry/Entity Type

Hospitality

Contact Information for Business Card

Rozsa Tarkany
Bartender & Sommelier
Phone: (FR) +33 6 4827 3190
(HU) +36 70 918 6352

Font styles to use
Script

Requirements
Must have
• Some sign, I am a bartender and sommelier as well.
Nice to have
• black and white maybe with 1 or 2 extra color
Should not have
• very colourful, to many things on the card

```html
<!DOCTYPE html>
<html lang="en">
<head>
<meta charset="utf-8">
<title>Rozsa Tarkany — Business Card</title>
<link rel="stylesheet" href="https://fonts.googleapis.com/css2?family=Bebas+Neue&family=Josefin+Sans:wght@400&display=swap">
<style>
  :root {
    --backdrop: #dedede;
    --card: #161616;
    --ink: #ffffff;
    --accent: #c2bb3b;
    --line-white: #e8e8e8;
  }
  * { margin: 0; padding: 0; box-sizing: border-box; }
  html, body {
    width: 1200px;
    height: 1000px;
    overflow: hidden;
    background: var(--backdrop);
  }
  .stage {
    width: 1200px;
    height: 1000px;
    display: flex;
    align-items: center;
    justify-content: center;
  }
  .card {
    position: relative;
    width: 740px;
    height: 424px;
    background: var(--card);
    overflow: hidden;
    box-shadow: 0 10px 30px rgba(0,0,0,0.18);
  }
  .rule {
    position: absolute;
    height: 3px;
  }
  .rule--top {
    top: 96px;
    left: 0;
    width: 100%;
    background: var(--accent);
  }
  .sign-mark {
    position: absolute;
    top: 36px;
    right: 95px;
    width: 80px;
    height: 80px;
    background: var(--accent);
  }
  .name {
    position: absolute;
    top: 112px;
    left: 60px;
    font-family: "Bebas Neue", sans-serif;
    font-size: 88px;
    font-weight: 400;
    line-height: 1;
    letter-spacing: 2px;
    color: var(--ink);
    white-space: nowrap;
  }
  .role-row {
    position: absolute;
    top: 206px;
    left: 0;
    width: 100%;
    display: flex;
    align-items: center;
    gap: 16px;
  }
  .role-row .dash {
    height: 2px;
    background: var(--line-white);
  }
  .role-row .dash--left { width: 44px; }
  .role-row .dash--right { flex: 1; }
  .role {
    font-family: "Josefin Sans", sans-serif;
    font-size: 17px;
    letter-spacing: 1.5px;
    color: var(--accent);
    text-transform: uppercase;
    padding-top: 3px;
    white-space: nowrap;
  }
  .services {
    position: absolute;
    top: 240px;
    left: 60px;
    list-style: none;
    font-family: "Bebas Neue", sans-serif;
    font-size: 31px;
    line-height: 0.92;
    letter-spacing: 1.5px;
    color: var(--ink);
  }
  .rule--mid {
    top: 336px;
    left: 0;
    width: 100%;
    height: 2px;
    background: var(--accent);
  }
  .contacts {
    position: absolute;
    top: 350px;
    left: 60px;
    list-style: none;
    font-family: "Bebas Neue", sans-serif;
    font-size: 25px;
    line-height: 1;
    letter-spacing: 1.5px;
    color: var(--ink);
  }
</style>
</head>
<body>
<main class="stage">
  <article class="card">
    <div class="rule rule--top"></div>
    <div class="sign-mark" role="img" aria-label="Bartender and sommelier sign"></div>
    <h1 class="name">Rozsa Tarkany</h1>
    <div class="role-row">
      <span class="dash dash--left"></span>
      <span class="role">Bartender &amp; Sommelier</span>
      <span class="dash dash--right"></span>
    </div>
    <ul class="services">
      <li>Cocktail Parties</li>
      <li>Corporate Events</li>
      <li>Dinner Parties</li>
    </ul>
    <div class="rule rule--mid"></div>
    <ul class="contacts">
      <li>+33 6 4827 3190 (FR)</li>
      <li>+36 70 918 6352 (HU)</li>
    </ul>
  </article>
</main>
</body>
</html>
```